Web Site - Holloway-Strength.com

Design a 3 page web site for Holloway Strength. See attached design brief.
Holloway Strength - Web Site
www.holloway-strength.com

Design a 3 page web site for Holloway Strength, a small local fitness center that provided cardio and weights only (machines and free weights). There are no classes or other services offered at this facility. Holloway Strength is an affordable alternative to the big box, expensive fitness centers. It is small, local, convenient and a community oriented place to work out.
web site can be clean, simple and communicate basic information about the company and membership offers. Although the branding is black, orange and gray, the web site colors should be soft, light and neutral colors that will appeal to both men and women.
Text: Input generic text during design for each text area that will be modified later during the coding phase. The selected designer is expected to code the site and deliver all compressive files (images, files and code) for an unrestricted hand off and full ownership of all content by the client for future modifications by others.

Images
Images used can be generic royalty free images of people working out, on cardio machines, lifting on universal equipment, stretching or lifting weights or images with out people i.e a yoga mat, free weights, a row of cardio machines etc. This is an adults only facility - images can be a mix of men and women and of diverse multi ethnic backgrounds. Image of the actual gym are included below but should NOT be used on the web site.

Branding - See attached for vertical and horizontal logos for Holloway Strength. These can be used in any way and should be incorporated into the web site
WEB SITE OUTLINE
THREE web pages - Pages can be individual pages clicked through to each page from a navigation area but ALSO pages can be “blend together” into one long scrolling “home” or primary landing page.
1) Home Page with basic information
2) Membership Page (to be later integrated with Quillmark member software to show changing membership specials). - see example below - all text will change later
3) contact page - address - telephone number - google map directions
www.holloway-strength.com
Address:
Located in Tannery Brook Commons
418 E. Walnut Lane, Suite 305, Limerick PA 19468
Tel: 484-555-0172

Target Market(s)

Men and Women - Adults over 18,

Industry/Entity Type

Fitness, Work Out, Gym

Coding

Coded - Design and coding required

Number of Pages Required

3 page

Requirements
Must have
• See Project Brief
Should not have
• Dark Colors that feel too masculine

```html
<!DOCTYPE html>
<html lang="en">
<head>
<meta charset="UTF-8">
<title>Holloway Strength – Home</title>
<link href="https://fonts.googleapis.com/css2?family=Roboto:wght@400;500;700;800&display=swap" rel="stylesheet">
<style>
:root{
  --orange:#ff6a00;
  --orange-soft:#fde7d8;
  --ink:#2b2b2b;
  --text:#555a60;
  --muted:#6b7077;
  --line:#e6e7ea;
  --page:#f4f5f7;
  --white:#ffffff;
}
*{box-sizing:border-box;margin:0;padding:0}
html,body{width:1200px;height:945px;overflow:hidden}
body{font-family:"Roboto",sans-serif;color:var(--ink);background:var(--page);position:relative}
.wrap{width:700px;margin-left:250px;position:relative}

/* header */
.site-header{height:49px;background:var(--white);border-bottom:1px solid var(--line)}
.site-header .wrap{height:48px;display:flex;align-items:center}
.brand{display:flex;align-items:center;gap:9px}
.brand-dot{width:20px;height:20px;border-radius:50%;background:var(--orange)}
.brand-name{font-size:10px;font-weight:700;letter-spacing:.2px;line-height:1}
.brand-tag{font-size:7px;font-weight:500;color:var(--text);margin-top:2px}
.nav{position:absolute;left:301px;display:flex;gap:4px;font-size:10px;color:var(--text);font-weight:500}
.nav a{padding:7px 8px;border-radius:14px;text-decoration:none;color:inherit}
.nav a.active{background:#f2f2f3;color:var(--ink);font-weight:700;border:1px solid var(--line)}
.btn{display:inline-flex;align-items:center;height:30px;padding:0 12px;border-radius:16px;font-size:10px;font-weight:700;text-decoration:none}
.btn-primary{background:var(--orange);color:var(--white);box-shadow:0 3px 8px rgba(255,106,0,.25)}
.btn-ghost{background:var(--white);color:var(--ink);border:1px solid var(--line)}
.join{position:absolute;right:0}

/* hero */
.hero{height:250px;position:relative}
.eyebrow{position:absolute;top:30px;left:0;height:23px;padding:0 8px;border:1px solid var(--line);border-radius:12px;background:var(--white);font-size:8.75px;color:var(--text);display:flex;align-items:center}
.hero-title{position:absolute;top:60px;left:0;font-size:38px;font-weight:800;line-height:36px;letter-spacing:-.3px}
.hero-title .accent{color:var(--orange)}
.hero-lead{position:absolute;top:176px;left:0;width:345px;font-size:11px;line-height:18px;color:var(--text)}
.hero-actions{position:absolute;top:224px;left:0;display:flex;gap:8px}
.hero-actions .btn{height:31px}
.hero-note{position:absolute;top:265px;left:0;font-size:8px;color:var(--muted)}
.hero-photo{position:absolute;top:35px;right:0;width:306px;height:234px;border-radius:22px;background:linear-gradient(135deg,#e8ecef 0%,#b9c0c4 45%,#4d5559 100%)}

/* features */
.features{margin-top:56px;display:flex;gap:9px}
.card{flex:1;height:107px;background:var(--white);border:1px solid var(--line);border-radius:12px;padding:12px 12px}
.card-icon{width:29px;height:29px;border-radius:7px;background:var(--orange-soft);display:flex;align-items:center;justify-content:center}
.card h3{font-size:10px;font-weight:700;margin-top:9px}
.card p{font-size:9.5px;line-height:16px;color:var(--text);margin-top:3px}

/* focus section */
.focus{margin-top:23px;height:165px;position:relative}
.focus-photo{position:absolute;left:0;top:0;width:279px;height:165px;border:1px solid var(--line);border-radius:12px;background:var(--white);padding:0 0 10px 10px}
.focus-photo div{width:100%;height:100%;border-radius:10px 0 0 0;background:linear-gradient(160deg,#eceae6 0%,#9a9793 40%,#b58f6a 80%,#c9a57f 100%)}
.focus-text{position:absolute;left:291px;top:19px}
.focus-text h2{font-size:17px;font-weight:700}
.focus-text p{font-size:9.5px;line-height:17px;color:var(--text);width:330px;margin-top:6px}
.focus-actions{display:flex;gap:8px;margin-top:10px}
.focus-text .focus-note{font-size:8px;line-height:12px;color:var(--muted);margin-top:8px;width:auto}

/* call to action */
.cta{margin-top:15px;height:65px;border:1px solid var(--line);border-radius:14px;background:linear-gradient(100deg,#f7c7a6 0%,#fbe5d6 35%,#fbf9f7 60%,#fbf9f7 100%);display:flex;align-items:center;justify-content:space-between;padding:0 14px}
.cta h2{font-size:12.5px;font-weight:700}
.cta p{font-size:10px;color:var(--text);margin-top:6px}

/* footer */
.site-footer{position:absolute;top:764px;left:0;width:1200px;height:181px;background:var(--white);border-top:1px solid var(--line)}
.footer-grid{position:relative;height:132px}
.f-brand{position:absolute;top:13px;left:0}
.f-about{font-size:8px;line-height:13.5px;color:var(--text);width:265px;margin-top:8px}
.f-contact{position:absolute;left:291px;top:17px;font-size:7.5px;color:var(--text);line-height:13px}
.f-row{display:flex;gap:8px}
.f-row strong{color:var(--ink);font-weight:500}
.f-tel{position:absolute;top:67px;left:0}
.f-hours{position:absolute;left:500px;top:25px;font-size:7.5px;color:var(--text);line-height:13px}
.f-hours h4{font-size:7.5px;font-weight:500;color:var(--ink)}
.f-hours .gap{margin-top:9px}
.f-bottom{border-top:1px solid var(--line);padding-top:12px;font-size:7.5px;color:var(--text)}
</style>
</head>
<body>

<header class="site-header">
  <div class="wrap">
    <div class="brand">
      <span class="brand-dot"></span>
      <div><div class="brand-name">HOLLOWAY STRENGTH</div><div class="brand-tag">Cardio • Machines • Free Weights</div></div>
    </div>
    <nav class="nav"><a class="active" href="#">Home</a><a href="#">Membership</a><a href="#">Contact</a></nav>
    <a class="btn btn-primary join" href="#">Join Now</a>
  </div>
</header>

<main class="wrap">
  <section class="hero">
    <div class="eyebrow">Adults 18+ • Cardio &amp; weights only • Community focused</div>
    <h1 class="hero-title">STRONG.<br>SIMPLE.<br><span class="accent">LOCAL.</span></h1>
    <p class="hero-lead">Your neighborhood fitness center in Marrowdale. Affordable, convenient, and designed for focused training.</p>
    <div class="hero-actions"><a class="btn btn-primary" href="#">View Membership Options</a><a class="btn btn-ghost" href="#">Contact Us</a></div>
    <p class="hero-note">No contracts. No gimmicks. Just equipment that works and a place that feels welcoming.</p>
    <div class="hero-photo" role="img" aria-label="Adults running on treadmills in a bright gym"></div>
  </section>

  <section class="features">
    <article class="card">
      <div class="card-icon"><svg width="13" height="13" viewBox="0 0 14 14"><circle cx="7" cy="7" r="6" fill="none" stroke="#ff6a00" stroke-width="1.3"/><path d="M9 4.8c-.4-.5-1.1-.8-2-.8-1.1 0-1.8.5-1.8 1.3 0 1.8 3.8.9 3.8 2.8 0 .8-.8 1.4-2 1.4-.9 0-1.700-.3-2.1-.9M7 3v8" fill="none" stroke="#ff6a00" stroke-width="1.1" stroke-linecap="round"/></svg></div>
      <h3>Affordable Membership</h3>
      <p>No contracts. No gimmicks. Clear options that fit real schedules.</p>
    </article>
    <article class="card">
      <div class="card-icon"><svg width="13" height="13" viewBox="0 0 14 14"><path d="M2 4.5v5M4 3.5v7M10 3.5v7M12 4.5v5M4 7h6" stroke="#2b2b2b" stroke-width="1.4" stroke-linecap="round"/></svg></div>
      <h3>Cardio &amp; Free Weights</h3>
      <p>Everything you need. Nothing you don’t. Machines and free weights only.</p>
    </article>
    <article class="card">
      <div class="card-icon"><svg width="14" height="10" viewBox="0 0 16 10"><path d="M4 2 1 5l3 3 4-3 4 3 3-3-3-3-4 3z" fill="none" stroke="#2b2b2b" stroke-width="1.3" stroke-linejoin="round"/><path d="M8 5l2-1.5" stroke="#ff6a00" stroke-width="1.3"/></svg></div>
      <h3>Local Community</h3>
      <p>A clean, welcoming place to work out with friendly, neighborhood energy.</p>
    </article>
  </section>

  <section class="focus">
    <div class="focus-photo"><div role="img" aria-label="Dumbbell rack and weight bench on a wooden floor"></div></div>
    <div class="focus-text">
      <h2>Designed for Focused Training</h2>
      <p>Holloway Strength offers a streamlined environment built for consistency. Bring your plan, train efficiently, and get on with your day.</p>
      <div class="focus-actions"><a class="btn btn-primary" href="#">Explore Memberships</a><a class="btn btn-ghost" href="#">Get Directions</a></div>
      <p class="focus-note">Replace this paragraph with your preferred messaging during development.</p>
    </div>
  </section>

  <section class="cta">
    <div><h2>Ready to Get Started?</h2><p>Join today and keep your fitness routine simple, steady, and local.</p></div>
    <a class="btn btn-primary" href="#">Join Today</a>
  </section>
</main>

<footer class="site-footer">
  <div class="wrap">
    <div class="footer-grid">
      <div class="f-brand">
        <div class="brand"><span class="brand-dot"></span><div><div class="brand-name">HOLLOWAY STRENGTH</div><div class="brand-tag">Small. Local. Convenient.</div></div></div>
        <p class="f-about">Affordable cardio and weights only. No classes. No upsells. Just a clean, welcoming place to work out.</p>
      </div>
      <div class="f-contact">
        <div class="f-row">
          <svg width="9" height="11" viewBox="0 0 10 12"><path d="M5 11S1 7 1 4.5a4 4 0 0 1 8 0C9 7 5 11 5 11z" fill="none" stroke="#2b2b2b" stroke-width="1"/><circle cx="5" cy="4.5" r="1.3" fill="none" stroke="#2b2b2b"/></svg>
          <div><strong>Located in Tannery Brook Commons</strong><br>418 E. Walnut Lane, Suite 305<br>Marrowdale, PA 19580</div>
        </div>
        <div class="f-row f-tel">
          <svg width="9" height="9" viewBox="0 0 10 10"><path d="M2 1l2 2-1 1.2c.6 1.2 1.5 2.1 2.8 2.8L7 6l2 2-1.2 1.3C4.5 9 1 5.5.7 2.2z" fill="none" stroke="#2b2b2b" stroke-width=".9" stroke-linejoin="round"/></svg>
          <div><strong>Tel</strong> 484-555-0172</div>
        </div>
      </div>
      <div class="f-hours">
        <h4>Hours</h4>
        <p>Mon–Fri: 5am–10pm<br>Sat–Sun: 7am–8pm</p>
        <h4 class="gap">Note</h4>
        <p>Hours and membership details can be updated during<br>buildout.</p>
      </div>
    </div>
    <div class="f-bottom">© 2026 Holloway Strength. All rights reserved.</div>
  </div>
</footer>

</body>
</html>
```